Plakat-Design für Verkauf von Bio-zertifiziertem Saatgut
Zielgruppe
Wir sind ein Start Up und verkaufen BIO Zertifiziertes Saatgut für Gemüse, Kräuter, Heilpflanzen und essbare Sprossen etc. Zielgruppe ist vor allem die DIY Community von Jung bis Alt.
Aufgabenstellung
*** INFO*** Da es keine 'Kalender'-Projekte gibt, sollten wir das Projekt unter 'Plakat' einstellen ***INFO***
Wir sind auf der Suche nach einem Design für einen Monatskalender (Deckblatt, 12 Monate, Schlussblatt) der als ewiger Aussaatkalender fungieren soll (Keine Jahreszahlen, nur der Monat). Jeden Monat sollen die Sorten gezeigt werden die jetzt ausgesät werden können. Am Besten teilweise (nicht alle) als Illustrationen oder Bilder. Die Sorten orientieren sich an unserem Saatgutsortiment. Als Unterteilung kann man: 'Vorzucht im Haus', Frühbeet' und 'Direktsaat'
Die Informationen welche Samen wann ausgesät werden, kommen von uns. (Erstmal Platzhalter für das Design nutzen) Falls der Designer Erfahrung in diesem Bereich hat, kann er die Informationen auch selber einfügen. Sonst ist der Designer für Layout und Illustrationen/Bilder zuständig. Toll wäre wenn für jeden Monat noch eine 'Bauernweisheit' zum Thema Pflanzen / Aussaat / Garten hinzugefügt werden kann.
Das Design soll sich an unserer CI der Website www.keimfeld.de orientieren. Logo, Farben und Fonts (My-Everything, BW Mitga) sind im Anhang beigefügt. Auch die Vorlage der Druckerei ist beigefügt. Format: DIN A4 hoch (210 x 297 mm), beidseitig bedruckt so das man den Kalender auch Aufgeklappt nutzen kann.
Falls noch Informationen benötigt werden, dann meldet euch gerne!

```html
<!DOCTYPE html>
<html lang="de">
<head>
<meta charset="utf-8">
<title>Keimfeld Aussaatkalender – März und April</title>
<link rel="stylesheet" href="https://fonts.googleapis.com/css2?family=Montserrat:wght@400;500;800&family=Comfortaa:wght@400;500&family=Allura&family=Gochi+Hand&display=swap">
<style>
  :root{
    --header-bg:#e6ecdf;
    --brand-green:#6a9a3a;
    --ink:#1c1c1c;
    --item-ink:#4e3b22;
    --sow-house:#eeb07a;
    --sow-frame:#a7cc85;
    --sow-direct:#5b3c14;
    --panel-fill:rgba(246,240,228,.78);
    --panel-fill-green:rgba(236,242,226,.78);
    --info-bg:#e9efe5;
    --organic-green:#8fbf24;
  }
  *{margin:0;padding:0;box-sizing:border-box}
  html,body{width:1200px;height:3238px;overflow:hidden;background:#fff}
  body{position:relative;font-family:"Comfortaa",sans-serif}

  .calendar-page{position:absolute;left:42px;width:1115px;height:1577px;overflow:hidden}
  .calendar-page--march{top:36px}
  .calendar-page--april{top:1630px}

  .top-strip{position:absolute;left:0;top:0;width:100%;height:88px}
  .calendar-page--march .top-strip{background:linear-gradient(90deg,#4a3526,#6b4a34 30%,#7a5a3a 60%,#3f3325)}
  .calendar-page--april .top-strip{background:linear-gradient(90deg,#6d5a2e,#9a7a3d 35%,#7b8a3a 65%,#4d5a2a)}

  .page-header{position:absolute;left:0;top:88px;width:100%;height:261px;background:var(--header-bg)}
  .todo-title{position:absolute;left:40px;top:26px;font-family:"Montserrat",sans-serif;font-weight:800;font-size:23px;letter-spacing:.5px;color:var(--ink)}
  .veg-illustrations{position:absolute;left:40px;top:58px;width:548px;height:190px;border-radius:30px;
    background:radial-gradient(circle at 15% 55%,#a8c98a 0 9%,transparent 10%),radial-gradient(circle at 30% 20%,#e88a3a 0 6%,transparent 7%),
    radial-gradient(circle at 55% 45%,#3f6a2a 0 7%,transparent 8%),radial-gradient(circle at 75% 20%,#d03a2a 0 6%,transparent 7%),
    radial-gradient(circle at 40% 75%,#c9384a 0 6%,transparent 7%),radial-gradient(circle at 63% 78%,#8a3a6a 0 6%,transparent 7%),
    radial-gradient(circle at 88% 50%,#4a8a3a 0 6%,transparent 7%),radial-gradient(circle at 78% 80%,#6aa04a 0 6%,transparent 7%)}
  .brand{position:absolute;left:683px;top:60px;width:331px;height:140px;display:flex;flex-direction:column;align-items:center;justify-content:center;gap:18px}
  .brand-dot{width:70px;height:70px;border-radius:50%;background:var(--brand-green)}
  .brand-name{font-family:"Montserrat",sans-serif;font-weight:500;font-size:40px;letter-spacing:5px;color:var(--brand-green)}

  .scene-photo{position:absolute;left:0;top:349px;width:100%;height:1228px}
  .calendar-page--march .scene-photo{background:linear-gradient(160deg,#5f6f3a 0%,#4d5a30 30%,#6b6a3a 55%,#8a5a3a 75%,#3e3826 100%)}
  .calendar-page--april .scene-photo{background:linear-gradient(170deg,#7a6a3a 0%,#8e6f4a 25%,#5a6a3a 50%,#3f5a2a 75%,#2e3d22 100%)}

  .sow-column{position:absolute;width:316px;border:7px solid;background:var(--panel-fill);padding:38px 0 0 14px}
  .sow-column--house{left:45px;border-color:var(--sow-house)}
  .sow-column--frame{left:401px;border-color:var(--sow-frame);background:var(--panel-fill-green)}
  .sow-column--direct{left:752px;border-color:var(--sow-direct)}
  .calendar-page--march .sow-column{top:389px;height:584px}
  .calendar-page--april .sow-column{top:914px;height:581px}

  .sow-list{list-style:none}
  .sow-item{display:flex;align-items:center;height:47px;font-size:21px;color:var(--item-ink)}
  .veg-icon{width:44px;height:34px;border-radius:50%;margin-right:26px;flex:none}
  .veg-icon--radish{background:#c9384a}.veg-icon--carrot{background:#e88a3a}.veg-icon--pea{background:#7aa84a}
  .veg-icon--cabbage{background:#a8c98a}.veg-icon--celery{background:#9ccc6a}.veg-icon--spinach{background:#3f7a2a}
  .veg-icon--beet{background:#8a1f2e}.veg-icon--rocket{background:#5a8a3a}.veg-icon--onion{background:#9a3a6a}
  .veg-icon--eggplant{background:#4a2a5a}.veg-icon--asparagus{background:#7a9a4a}.veg-icon--fennel{background:#cfe2b0}
  .mark{margin-left:14px;width:16px;height:16px;flex:none}

  .month-name{position:absolute;font-family:"Allura",cursive;color:#fff;font-size:150px;line-height:1}
  .calendar-page--march .month-name{left:75px;top:990px;transform:rotate(-8deg)}
  .calendar-page--april .month-name{left:405px;top:445px;transform:rotate(-8deg)}

  .good-to-know{position:absolute;width:396px;height:364px;background:var(--info-bg);padding:18px 0 0 32px}
  .calendar-page--march .good-to-know{left:54px;top:1168px}
  .calendar-page--april .good-to-know{left:676px;top:441px}
  .good-to-know h2{font-family:"Montserrat",sans-serif;font-weight:800;font-size:22px;letter-spacing:.5px;color:var(--ink);margin-bottom:12px}
  .legend{list-style:none}
  .legend-row{display:flex;align-items:center;height:41px;font-family:"Montserrat",sans-serif;font-size:19px;letter-spacing:1.5px;color:#2a2a2a}
  .legend-swatch{width:75px;height:22px;margin-right:28px}
  .legend-swatch--house{background:var(--sow-house)}
  .legend-swatch--frame{background:var(--sow-frame)}
  .legend-swatch--direct{background:var(--sow-direct)}
  .symbol-key{list-style:none;margin-top:8px}
  .symbol-row{display:flex;align-items:center;height:32px;font-size:18px;color:#2a2a2a}
  .symbol-row svg{width:22px;height:22px;margin-right:12px}
  .organic-note{margin-top:24px;width:245px}
  .organic-note strong{display:block;font-family:"Montserrat",sans-serif;font-weight:500;font-size:15px;color:#1c1c1c;margin-bottom:4px}
  .organic-note p{font-family:"Montserrat",sans-serif;font-size:12px;line-height:1.35;color:#333}
  .organic-badge{position:absolute;width:160px;height:148px}
  .calendar-page--march .organic-badge{left:324px;top:1063px+0}
  .calendar-page--march .organic-badge{top:1415px}
  .calendar-page--april .organic-badge{left:945px;top:690px}

  .saying{position:absolute;display:flex;align-items:center;justify-content:center;text-align:center;font-family:"Gochi Hand",cursive;color:#f2f2f2;line-height:1.3}
  .saying--stone{left:842px;top:1295px;width:265px;height:282px;border-radius:48% 44% 6% 6%/30% 30% 4% 4%;background:linear-gradient(160deg,#6a6c6c,#4a4c4c 60%,#3a3a3a);font-size:30px;padding:20px}
  .saying--chalkboard{left:670px;top:1336px;width:320px;height:225px;background:#1f2022;border:14px solid #8a7a62;font-size:31px;padding:10px}
</style>
</head>
<body>

<section class="calendar-page calendar-page--march" aria-label="Kalenderblatt März">
  <div class="top-strip" role="img" aria-label="Foto: Gartenerde mit Herbstlaub"></div>
  <header class="page-header">
    <h1 class="todo-title">TO DO LIST</h1>
    <div class="veg-illustrations" role="img" aria-label="Illustrationen: Möhren, Sellerie, Tomaten, Kohl, Zucchini, Gurke, Spinat, Radieschen, Zwiebel, Erbsen"></div>
    <div class="brand"><span class="brand-dot"></span><span class="brand-name">KEIMFELD</span></div>
  </header>
  <div class="scene-photo" role="img" aria-label="Foto: Kind mit Mütze gräbt mit einer Hacke im Gartenbeet"></div>

  <div class="sow-column sow-column--house">
    <ul class="sow-list">
      <li class="sow-item"><span class="veg-icon veg-icon--radish" role="img" aria-label="Radieschen-Illustration"></span>Radieschen</li>
      <li class="sow-item"><span class="veg-icon veg-icon--carrot" role="img" aria-label="Möhren-Illustration"></span>Frühe Möhre<svg class="mark" viewBox="0 0 16 16"><path d="M6 15 C6 9 4 5 1 2 M6 10 C8 6 11 4 14 4" stroke="#1c1c1c" stroke-width="2" fill="none"/></svg></li>
      <li class="sow-item"><span class="veg-icon veg-icon--pea" role="img" aria-label="Erbsen-Illustration"></span>Zuckererbse<svg class="mark" viewBox="0 0 16 16"><circle cx="8" cy="8" r="4.5" fill="#111"/><g stroke="#111" stroke-width="1.5"><path d="M8 0v2M8 14v2M0 8h2M14 8h2M2 2l1.5 1.5M12.5 12.5L14 14M2 14l1.5-1.5M12.5 3.5L14 2"/></g></svg></li>
      <li class="sow-item"><span class="veg-icon veg-icon--cabbage" role="img" aria-label="Weißkohl-Illustration"></span>Weißkohl</li>
      <li class="sow-item"><span class="veg-icon veg-icon--celery" role="img" aria-label="Sellerie-Illustration"></span>Stangenellerie</li>
    </ul>
  </div>
  <div class="sow-column sow-column--frame">
    <ul class="sow-list">
      <li class="sow-item"><span class="veg-icon veg-icon--spinach" role="img" aria-label="Spinat-Illustration"></span>Spinat</li>
      <li class="sow-item"><span class="veg-icon veg-icon--beet" role="img" aria-label="Rote-Bete-Illustration"></span>Rote Bete</li>
      <li class="sow-item"><span class="veg-icon veg-icon--rocket" role="img" aria-label="Rucola-Illustration"></span>Rucola</li>
    </ul>
  </div>
  <div class="sow-column sow-column--direct">
    <ul class="sow-list">
      <li class="sow-item"><span class="veg-icon veg-icon--onion" role="img" aria-label="Zwiebel-Illustration"></span>Steckzwiebel<svg class="mark" viewBox="0 0 16 16"><path d="M6 15 C6 9 4 5 1 2 M6 10 C8 6 11 4 14 4" stroke="#1c1c1c" stroke-width="2" fill="none"/></svg></li>
      <li class="sow-item"><span class="veg-icon veg-icon--eggplant" role="img" aria-label="Auberginen-Illustration"></span>Aubergine<svg class="mark" viewBox="0 0 16 16"><circle cx="8" cy="8" r="4.5" fill="#111"/><g stroke="#111" stroke-width="1.5"><path d="M8 0v2M8 14v2M0 8h2M14 8h2M2 2l1.5 1.5M12.5 12.5L14 14M2 14l1.5-1.5M12.5 3.5L14 2"/></g></svg></li>
      <li class="sow-item"><span class="veg-icon veg-icon--asparagus" role="img" aria-label="Spargel-Illustration"></span>Spargel</li>
      <li class="sow-item"><span class="veg-icon veg-icon--fennel" role="img" aria-label="Fenchel-Illustration"></span>Fenchel</li>
    </ul>
  </div>

  <div class="month-name">März</div>

  <aside class="good-to-know">
    <h2>GOOD TO KNOW</h2>
    <ul class="legend">
      <li class="legend-row"><span class="legend-swatch legend-swatch--house"></span>VORZUCHT IM HAUS</li>
      <li class="legend-row"><span class="legend-swatch legend-swatch--frame"></span>FRÜHBEET</li>
      <li class="legend-row"><span class="legend-swatch legend-swatch--direct"></span>DIREKTSAAT</li>
    </ul>
    <ul class="symbol-key">
      <li class="symbol-row"><svg viewBox="0 0 16 16"><path d="M6 15 C6 9 4 5 1 2 M6 10 C8 6 11 4 14 4" stroke="#1c1c1c" stroke-width="2" fill="none"/></svg>Anpflanzung erfordert Vorkeimen</li>
      <li class="symbol-row"><svg viewBox="0 0 16 16"><circle cx="8" cy="8" r="4.5" fill="#111"/><g stroke="#111" stroke-width="1.5"><path d="M8 0v2M8 14v2M0 8h2M14 8h2M2 2l1.5 1.5M12.5 12.5L14 14M2 14l1.5-1.5M12.5 3.5L14 2"/></g></svg>Lichtkeimer</li>
    </ul>
    <div class="organic-note">
      <strong>Pflanzen mit grünem Gewissen</strong>
      <p>BIO-Zertifikat, welches gewährleistet, dass das Saatgut den höchsten Qualitätsstandards entspricht.</p>
    </div>
  </aside>
  <svg class="organic-badge" viewBox="0 0 160 148" aria-hidden="true"><path d="M80 140 C30 105 4 78 4 46 C4 20 24 4 46 4 C62 4 74 14 80 26 C86 14 98 4 114 4 C136 4 156 20 156 46 C156 78 130 105 80 140Z" fill="var(--organic-green)"/></svg>

  <div class="saying saying--stone" role="img" aria-label="Foto: Schieferstein mit Bauernweisheit"><span>Fürchte nicht den Schnee im März, darunter schlägt ein warmes Herz.</span></div>
</section>

<section class="calendar-page calendar-page--april" aria-label="Kalenderblatt April">
  <div class="top-strip" role="img" aria-label="Foto: Herbstliche Blätter und Blüten"></div>
  <header class="page-header">
    <h1 class="todo-title">TO DO LIST</h1>
    <div class="veg-illustrations" role="img" aria-label="Illustrationen: Möhren, Sellerie, Tomaten, Kohl, Zucchini, Gurke, Spinat, Radieschen, Zwiebel, Erbsen"></div>
    <div class="brand"><span class="brand-dot"></span><span class="brand-name">KEIMFELD</span></div>
  </header>
  <div class="scene-photo" role="img" aria-label="Foto: Kind im karierten Hemd greift nach Blüten im Strauch"></div>

  <aside class="good-to-know">
    <h2>GOOD TO KNOW</h2>
    <ul class="legend">
      <li class="legend-row"><span class="legend-swatch legend-swatch--house"></span>VORZUCHT IM HAUS</li>
      <li class="legend-row"><span class="legend-swatch legend-swatch--frame"></span>FRÜHBEET</li>
      <li class="legend-row"><span class="legend-swatch legend-swatch--direct"></span>DIREKTSAAT</li>
    </ul>
    <ul class="symbol-key">
      <li class="symbol-row"><svg viewBox="0 0 16 16"><path d="M6 15 C6 9 4 5 1 2 M6 10 C8 6 11 4 14 4" stroke="#1c1c1c" stroke-width="2" fill="none"/></svg>Anpflanzung erfordert Vorkeimen</li>
      <li class="symbol-row"><svg viewBox="0 0 16 16"><circle cx="8" cy="8" r="4.5" fill="#111"/><g stroke="#111" stroke-width="1.5"><path d="M8 0v2M8 14v2M0 8h2M14 8h2M2 2l1.5 1.5M12.5 12.5L14 14M2 14l1.5-1.5M12.5 3.5L14 2"/></g></svg>Lichtkeimer</li>
    </ul>
    <div class="organic-note">
      <strong>Pflanzen mit grünem Gewissen</strong>
      <p>BIO-Zertifikat, welches gewährleistet, dass das Saatgut den höchsten Qualitätsstandards entspricht.</p>
    </div>
  </aside>
  <svg class="organic-badge" viewBox="0 0 160 148" aria-hidden="true"><path d="M80 140 C30 105 4 78 4 46 C4 20 24 4 46 4 C62 4 74 14 80 26 C86 14 98 4 114 4 C136 4 156 20 156 46 C156 78 130 105 80 140Z" fill="var(--organic-green)"/></svg>

  <div class="month-name">April</div>

  <div class="sow-column sow-column--house">
    <ul class="sow-list">
      <li class="sow-item"><span class="veg-icon veg-icon--radish" role="img" aria-label="Radieschen-Illustration"></span>Radieschen</li>
      <li class="sow-item"><span class="veg-icon veg-icon--carrot" role="img" aria-label="Möhren-Illustration"></span>Frühe Möhre<svg class="mark" viewBox="0 0 16 16"><path d="M6 15 C6 9 4 5 1 2 M6 10 C8 6 11 4 14 4" stroke="#1c1c1c" stroke-width="2" fill="none"/></svg></li>
      <li class="sow-item"><span class="veg-icon veg-icon--pea" role="img" aria-label="Erbsen-Illustration"></span>Zuckererbse<svg class="mark" viewBox="0 0 16 16"><circle cx="8" cy="8" r="4.5" fill="#111"/><g stroke="#111" stroke-width="1.5"><path d="M8 0v2M8 14v2M0 8h2M14 8h2M2 2l1.5 1.5M12.5 12.5L14 14M2 14l1.5-1.5M12.5 3.5L14 2"/></g></svg></li>
      <li class="sow-item"><span class="veg-icon veg-icon--cabbage" role="img" aria-label="Weißkohl-Illustration"></span>Weißkohl</li>
      <li class="sow-item"><span class="veg-icon veg-icon--celery" role="img" aria-label="Sellerie-Illustration"></span>Stangenellerie</li>
    </ul>
  </div>
  <div class="sow-column sow-column--frame">
    <ul class="sow-list">
      <li class="sow-item"><span class="veg-icon veg-icon--spinach" role="img" aria-label="Spinat-Illustration"></span>Spinat</li>
      <li class="sow-item"><span class="veg-icon veg-icon--beet" role="img" aria-label="Rote-Bete-Illustration"></span>Rote Bete</li>
      <li class="sow-item"><span class="veg-icon veg-icon--rocket" role="img" aria-label="Rucola-Illustration"></span>Rucola</li>
    </ul>
  </div>
  <div class="sow-column sow-column--direct">
    <ul class="sow-list">
      <li class="sow-item"><span class="veg-icon veg-icon--onion" role="img" aria-label="Zwiebel-Illustration"></span>Steckzwiebel<svg class="mark" viewBox="0 0 16 16"><path d="M6 15 C6 9 4 5 1 2 M6 10 C8 6 11 4 14 4" stroke="#1c1c1c" stroke-width="2" fill="none"/></svg></li>
      <li class="sow-item"><span class="veg-icon veg-icon--eggplant" role="img" aria-label="Auberginen-Illustration"></span>Aubergine<svg class="mark" viewBox="0 0 16 16"><circle cx="8" cy="8" r="4.5" fill="#111"/><g stroke="#111" stroke-width="1.5"><path d="M8 0v2M8 14v2M0 8h2M14 8h2M2 2l1.5 1.5M12.5 12.5L14 14M2 14l1.5-1.5M12.5 3.5L14 2"/></g></svg></li>
      <li class="sow-item"><span class="veg-icon veg-icon--asparagus" role="img" aria-label="Spargel-Illustration"></span>Spargel</li>
      <li class="sow-item"><span class="veg-icon veg-icon--fennel" role="img" aria-label="Fenchel-Illustration"></span>Fenchel</li>
    </ul>
  </div>

  <div class="saying saying--chalkboard" role="img" aria-label="Foto: Kreidetafel mit Bauernweisheit"><span>April und Weiberwill ändern sich schnell und viel.</span></div>
</section>

</body>
</html>
```